church business card design

we have a logo and would like our business card to complement the logo. we would prefer the logo in white on a coloured background - probably blue. Under the logo or near it we would have the Words 'Love God. Love people. Follow Jesus.'
We would like some yellow/gold highlights. We like the design by mintaro quill 4821 front of card - https://www.pelvarostudio.com/businesscard-design/contest/5812094

Our church is multicultural, inner city, friendly, warm welcoming and that's the feel we would like. there's also an element of being spontaneous, so a swirl or swoosh might help give that feel. the example card above had some curved shapes on the front of the card for example.
on the second side of the card would have the details of the Senior Pastor and the contact details for the church.
after the business card we would be looking at letterhead and an A5 flyer for printing but also as document templates so we can create invitations etc going forward

```html
<!DOCTYPE html>
<html lang="en">
<head>
<meta charset="utf-8">
<title>Harbor Stone Church – Business Card</title>
<link rel="stylesheet" href="https://fonts.googleapis.com/css2?family=Montserrat:wght@500;700&family=Roboto:wght@400;500&display=swap">
<style>
  :root {
    --bg: #e4e4e4;
    --blue: #263f8f;
    --ink: #1b1b1b;
    --paper: #ffffff;
    --muted: #d9d9d9;
  }
  * { box-sizing: border-box; margin: 0; padding: 0; }
  html, body { width: 1200px; height: 900px; overflow: hidden; }
  body {
    background: var(--bg);
    font-family: "Roboto", Arial, sans-serif;
    position: relative;
  }
  .card {
    position: absolute;
    left: 285px;
    width: 630px;
    height: 360px;
    border-radius: 22px;
    overflow: hidden;
    box-shadow: 0 6px 14px rgba(0,0,0,.18);
  }
  .card-front { top: 55px; background: var(--blue); color: var(--paper); }
  .card-back { top: 480px; background: var(--paper); color: var(--ink); }

  .wordmark { font-family: "Montserrat", Arial, sans-serif; font-weight: 500; line-height: 1; }
  .front-mark {
    position: absolute; left: 0; right: 0; top: 112px; text-align: center;
  }
  .front-mark .wordmark-name { font-size: 54px; letter-spacing: 1px; }
  .front-mark .wordmark-sub { font-size: 20px; letter-spacing: 22px; margin-top: 10px; padding-left: 22px; }
  .tagline {
    position: absolute; left: 0; right: 0; top: 262px; text-align: center;
    font-size: 19px; letter-spacing: .5px;
  }
  .tagline .sep { margin: 0 10px; }

  .back-mark { position: absolute; left: 44px; top: 36px; }
  .back-mark .wordmark-name { font-size: 40px; }
  .back-mark .wordmark-sub { font-size: 15px; letter-spacing: 16px; margin-top: 8px; padding-left: 40px; }

  .scene { position: absolute; inset: 0; }
  .person-tab { position: absolute; left: 0; top: 178px; width: 26px; height: 48px; background: var(--ink); }
  .person { position: absolute; left: 44px; top: 172px; }
  .person-name { font-family: "Montserrat", Arial, sans-serif; font-weight: 700; font-size: 31px; letter-spacing: .5px; }
  .person-role { font-size: 19px; margin-top: 2px; }
  .contacts { position: absolute; left: 44px; top: 252px; list-style: none; font-size: 17px; }
  .contacts li { display: flex; align-items: center; gap: 10px; height: 25px; }
  .contacts svg { width: 14px; height: 14px; fill: var(--ink); }
  .address {
    position: absolute; right: 30px; top: 238px; color: var(--paper);
    font-size: 15px; line-height: 1.35; text-align: right;
  }
</style>
</head>
<body>
  <section class="card card-front" aria-label="Business card front">
    <div class="front-mark wordmark">
      <div class="wordmark-name">Harbor Stone</div>
      <div class="wordmark-sub">CHURCH</div>
    </div>
    <p class="tagline">Love God<span class="sep">|</span>Love people<span class="sep">|</span>Follow Jesus</p>
  </section>

  <section class="card card-back" aria-label="Business card back">
    <svg class="scene" viewBox="0 0 630 360" preserveAspectRatio="none">
      <rect x="410" y="22" width="150" height="170" rx="10" fill="var(--muted)" role="img" aria-label="Cross silhouette standing on a hilltop"/>
      <path d="M0 330 L330 330 C395 330 400 250 430 215 C455 185 480 175 510 165 C560 150 600 150 630 140 L630 360 L0 360 Z" fill="var(--ink)"/>
    </svg>
    <div class="back-mark wordmark">
      <div class="wordmark-name">Harbor Stone</div>
      <div class="wordmark-sub">CHURCH</div>
    </div>
    <div class="person-tab"></div>
    <div class="person">
      <div class="person-name">DANIEL REYES</div>
      <div class="person-role">Senior Pastor</div>
    </div>
    <ul class="contacts">
      <li><svg viewBox="0 0 24 24"><path d="M6.6 10.8a15.1 15.1 0 0 0 6.6 6.6l2.2-2.2a1 1 0 0 1 1-.25 11.4 11.4 0 0 0 3.6.57 1 1 0 0 1 1 1V20a1 1 0 0 1-1 1A17 17 0 0 1 3 4a1 1 0 0 1 1-1h3.5a1 1 0 0 1 1 1c0 1.25.2 2.45.57 3.57a1 1 0 0 1-.25 1z"/></svg>(555) 204 8813</li>
      <li><svg viewBox="0 0 24 24"><path d="M2 5h20v14H2z M2 5l10 8 10-8" /></svg>hello@harborstone.org</li>
      <li><svg viewBox="0 0 24 24"><circle cx="12" cy="12" r="10"/><path d="M2 12h20M12 2c3 3 3 17 0 20M12 2c-3 3-3 17 0 20" stroke="#fff" stroke-width="1.5" fill="none"/></svg>www.harborstone.org</li>
    </ul>
    <address class="address" style="font-style:normal">Unit 8, 17 Wharf Lane<br>Eastgate DKR 3052</address>
  </section>
</body>
</html>
```